business card - for laser marking

I need design (curve) for my business card (make with laser) size 85mm x 55mm. How it look business card with laser marking see attached picture.

color:
Background: white
text and icons black

Please include: one side
1. dominik vrhovec - direktor
2. phone: +386(0)41 726 193
+386(0)592 817 06
3. info@zlatorez.example
4. faecebook.com/Zlatorez.Ex
5. KP-ATELJE, Dominik Vrhovec s.p.
Brezova ulica 17, 1000 Ljubljana, SI
6. logo

Please include: second side
1. logo
2. www.zlatorez.example
3. Lasersko graviranje
ovitki telefonov, ohišja telefonov / tablic, nakit, ure, alu vizitke, dog-tagi, kemični svinčniki, orodja, noži, vžigalniki

Industry/Entity Type

Business

Contact Information for Business Card

Please include: one side
+386(0)592 817 06
3. info@zlatorez.example
6. logo

1. logo
2. www.zlatorez.example
3. Lasersko graviranje

Colors
000000
ffffff

Requirements
Must have
• I need design (curve) for my business card (make with laser) size 85mm x 55mm. How it look business card with laser marking see attached picture.
• color:
• Background: white
• text and icons black
• Please include: one side
• 1. dominik vrhovec - direktor
• 2. phone: +386(0)41 726 193
• +386(0)592 817 06
• 3. info@zlatorez.example
• 4. faecebook.com/Zlatorez.Ex
• 5. KP-ATELJE, Dominik Vrhovec s.p.
• Brezova ulica 17, 1000 Ljubljana, SI
• 6. logo
• Please include: second side
• 1. logo
• 2. www.zlatorez.example
• 3. Lasersko graviranje
• ovitki telefonov, ohišja telefonov / tablic, nakit, ure, alu vizitke, dog-tagi, kemični svinčniki, orodja, noži, vžigalniki

```html
<!DOCTYPE html>
<html lang="sl">
<head>
<meta charset="utf-8">
<title>Zlatorez – vizitka</title>
<link rel="stylesheet" href="https://fonts.googleapis.com/css2?family=Play:wght@400;700&display=swap">
<style>
  :root {
    --stage: #3a3a3a;
    --card: #ffffff;
    --ink: #111111;
  }
  * { box-sizing: border-box; margin: 0; padding: 0; }
  html, body { width: 1000px; height: 1200px; overflow: hidden; }
  body {
    background: var(--stage);
    font-family: "Play", sans-serif;
    color: var(--ink);
    position: relative;
  }
  .card {
    position: absolute;
    background: var(--card);
  }
  .card--front {
    left: 155px; top: 111px; width: 672px; height: 431px;
    border-radius: 0 38px 0 38px;
  }
  .card--back {
    left: 152px; top: 636px; width: 678px; height: 436px;
    border-radius: 38px 0 38px 0;
  }
  .holder-name {
    position: absolute; left: 56px; top: 55px;
    font-size: 23px; letter-spacing: 1.5px; white-space: nowrap;
  }
  .holder-role {
    position: absolute; left: 56px; top: 89px; font-size: 17px;
  }
  .contact-list {
    position: absolute; left: 56px; list-style: none; font-size: 17px;
  }
  .contact-list li {
    display: flex; align-items: center; gap: 9px; height: 24px; white-space: nowrap;
  }
  .contact-list--phones { top: 147px; }
  .contact-list--phones li { height: 29px; }
  .contact-list--online { top: 258px; }
  .contact-list--address { top: 350px; }
  .contact-list--address li { align-items: flex-start; height: auto; line-height: 23px; }
  .icon { width: 17px; height: 17px; flex: none; fill: var(--ink); }
  .contact-list--address .icon { margin-top: 3px; }
  .brand {
    position: absolute; display: flex; align-items: center; gap: 10px;
    font-size: 32px; font-weight: 700; letter-spacing: 1px; white-space: nowrap;
  }
  .brand-dot { width: 18px; height: 18px; border-radius: 50%; background: var(--ink); }
  .card--front .brand { left: 375px; top: 168px; }
  .card--back .brand { left: 50%; top: 143px; transform: translateX(-50%); }
  .services {
    position: absolute; left: 0; right: 0; top: 258px;
    text-align: center; font-size: 17px; line-height: 35px;
  }
</style>
</head>
<body>
  <section class="card card--front" aria-label="Sprednja stran vizitke">
    <h1 class="holder-name">DOMINIK VRHOVEC</h1>
    <p class="holder-role">direktor</p>

    <ul class="contact-list contact-list--phones">
      <li><svg class="icon" viewBox="0 0 24 24" aria-hidden="true"><path d="M6.6 10.8a15.1 15.1 0 0 0 6.6 6.6l2.2-2.2c.3-.3.7-.4 1-.2 1.1.4 2.3.6 3.6.6.6 0 1 .4 1 1V20c0 .6-.4 1-1 1A17 17 0 0 1 3 4c0-.6.4-1 1-1h3.5c.6 0 1 .4 1 1 0 1.3.2 2.5.6 3.6.1.3 0 .7-.2 1z"/></svg>+386(0)41 726 193</li>
      <li><svg class="icon" viewBox="0 0 24 24" aria-hidden="true"><path d="M6.6 10.8a15.1 15.1 0 0 0 6.6 6.6l2.2-2.2c.3-.3.7-.4 1-.2 1.1.4 2.3.6 3.6.6.6 0 1 .4 1 1V20c0 .6-.4 1-1 1A17 17 0 0 1 3 4c0-.6.4-1 1-1h3.5c.6 0 1 .4 1 1 0 1.3.2 2.5.6 3.6.1.3 0 .7-.2 1z"/></svg>+386(0)592 817 06</li>
    </ul>

    <ul class="contact-list contact-list--online">
      <li><svg class="icon" viewBox="0 0 24 24" aria-hidden="true"><rect x="3" y="3" width="18" height="18" rx="2"/></svg>Zlatorez.Ex</li>
      <li><svg class="icon" viewBox="0 0 24 24" aria-hidden="true"><path d="M2 5h20v14H2z M3.5 6.5v.4l8.5 6 8.5-6v-.4z" fill-rule="evenodd"/></svg>info@zlatorez.example</li>
    </ul>

    <ul class="contact-list contact-list--address">
      <li><svg class="icon" viewBox="0 0 24 24" aria-hidden="true"><path d="M12 2a7 7 0 0 0-7 7c0 5 7 13 7 13s7-8 7-13a7 7 0 0 0-7-7zm0 9.5A2.5 2.5 0 1 1 12 6.5a2.5 2.5 0 0 1 0 5z"/></svg>
        <span>KP-ATELJE, Dominik Vrhovec s.p.<br>Brezova ulica 17, 1000 Ljubljana, SI</span></li>
    </ul>

    <div class="brand"><span class="brand-dot"></span>ZLATOREZ</div>
  </section>

  <section class="card card--back" aria-label="Zadnja stran vizitke">
    <div class="brand"><span class="brand-dot"></span>ZLATOREZ</div>
    <div class="services">
      <p>www.zlatorez.example</p>
      <p>Lasersko graviranje</p>
      <p>ovitki telefonov, ohišja telefonov / tablic, nakit, ure, alu vizitke</p>
      <p>dog-tagi, kemični svinčniki, orodja, noži, vžigalniki</p>
    </div>
  </section>
</body>
</html>
```